Poster design for Belgian waffles

We are a local frozen yogurt chain that will introduce a new product for winter. It is Belgian waffle. You can have it a plain, with toppings such fresh fruit or with our frozen yogurt. We need two posters, one for introduction of the product and one that has pricing on it.

Target Market(s)

College students and young professionals

Industry/Entity Type

Pricing

```html
<!DOCTYPE html>
<html lang="en">
<head>
<meta charset="utf-8">
<title>Belgian Waffle Poster</title>
<link rel="stylesheet" href="https://fonts.googleapis.com/css2?family=Fira+Sans+Condensed:wght@500;600&family=Open+Sans:wght@600;700&display=swap">
<style>
  :root {
    --page: #ffffff;
    --frame: #000000;
    --panel-light: #f3f3f3;
    --panel-mid: #dcdcdc;
    --panel-edge: #b4b4b4;
    --divider: #3a3a3a;
    --tab-top: #ff4a1c;
    --tab-bottom: #c41a06;
    --tab-text: #ffffff;
    --headline: #5b7a2b;
    --waffle-text: #e98b1c;
    --waffle-dark: #c4610f;
    --brand: #7a7a7a;
    --price-text: #9a9a9a;
    --bullet: #8c8c8c;
    --photo-a: #f3b453;
    --photo-b: #c8382e;
  }
  * { margin: 0; padding: 0; box-sizing: border-box; }
  html, body { width: 1200px; height: 1200px; overflow: hidden; background: var(--page); }
  .canvas {
    position: relative; width: 1200px; height: 1200px;
    background: var(--page); border: 8px solid var(--frame);
  }
  .poster {
    position: absolute; left: 166px; top: 28px; width: 862px; height: 1118px;
    overflow: hidden;
    font-family: "Fira Sans Condensed", "Open Sans", sans-serif;
  }
  .band {
    position: absolute; left: 0; width: 100%;
    background: linear-gradient(90deg, var(--panel-edge) 0%, var(--panel-mid) 12%, var(--panel-light) 50%, var(--panel-mid) 88%, var(--panel-edge) 100%);
  }
  .band--header { top: 0; height: 204px; }
  .band--feature { top: 206px; height: 572px; }
  .band--prices { top: 780px; height: 338px; }
  .divider { position: absolute; left: 0; width: 100%; height: 2px; background: var(--divider); }
  .divider--top { top: 204px; }
  .divider--bottom { top: 778px; }
  .new-tab {
    position: absolute; left: 328px; top: 0; width: 194px; height: 74px;
    background: linear-gradient(180deg, var(--tab-top), var(--tab-bottom));
    border-radius: 0 0 12px 12px;
    color: var(--tab-text); font-family: "Open Sans", sans-serif; font-weight: 700;
    font-size: 40px; line-height: 74px; text-align: center; letter-spacing: 1px;
  }
  .headline {
    position: absolute; left: 0; top: 112px; width: 100%; text-align: center;
    color: var(--headline); font-weight: 600; font-size: 60px; line-height: 1; letter-spacing: 0.5px;
  }
  .product-name {
    position: absolute; font-family: "Open Sans", sans-serif; font-weight: 600;
    color: var(--waffle-text); line-height: 1; letter-spacing: -2px; font-size: 142px;
    -webkit-text-stroke: 2px var(--waffle-dark);
  }
  .product-name--first { left: 92px; top: 292px; }
  .product-name--second { left: 340px; top: 416px; }
  .product-photo {
    position: absolute; left: 72px; top: 444px; width: 246px; height: 150px;
    border-radius: 20px;
    background: radial-gradient(ellipse at 65% 50%, var(--photo-a) 0%, #e7a040 45%, rgba(200,56,46,0.55) 80%, rgba(243,243,243,0) 100%);
  }
  .brand {
    position: absolute; left: 246px; top: 596px; width: 522px; text-align: center;
    font-weight: 600; font-size: 84px; line-height: 1; letter-spacing: 6px;
    color: var(--brand);
  }
  .price-list { position: absolute; left: 69px; top: 846px; list-style: none; }
  .price-list__item {
    display: flex; align-items: center; height: 72px;
    color: var(--price-text); font-weight: 500; font-size: 42px; white-space: nowrap;
  }
  .price-list__icon { width: 26px; height: 26px; margin-right: 25px; flex: none; }
</style>
</head>
<body>
  <div class="canvas">
    <div class="poster">
      <div class="band band--header"></div>
      <div class="band band--feature"></div>
      <div class="band band--prices"></div>
      <div class="divider divider--top"></div>
      <div class="divider divider--bottom"></div>

      <div class="new-tab">NEW</div>
      <h1 class="headline">INTRODUCING THE DELICIOUS</h1>

      <div class="product-name product-name--first">Belgian</div>
      <div class="product-name product-name--second">Waffle</div>

      <div class="product-photo" role="img" aria-label="Photo of golden Belgian waffles with a fresh strawberry and blueberries"></div>

      <div class="brand">Frostcup</div>

      <ul class="price-list">
        <li class="price-list__item">
          <svg class="price-list__icon" viewBox="0 0 26 26" aria-hidden="true"><circle cx="13" cy="13" r="12" fill="var(--bullet)"/><path d="M10 7 L17 13 L10 19" fill="none" stroke="#f0f0f0" stroke-width="3" stroke-linecap="round" stroke-linejoin="round"/></svg>
          Waffle: $2.57
        </li>
        <li class="price-list__item">
          <svg class="price-list__icon" viewBox="0 0 26 26" aria-hidden="true"><circle cx="13" cy="13" r="12" fill="var(--bullet)"/><path d="M10 7 L17 13 L10 19" fill="none" stroke="#f0f0f0" stroke-width="3" stroke-linecap="round" stroke-linejoin="round"/></svg>
          Waffle with toppings or yogurt: $4.53
        </li>
        <li class="price-list__item">
          <svg class="price-list__icon" viewBox="0 0 26 26" aria-hidden="true"><circle cx="13" cy="13" r="12" fill="var(--bullet)"/><path d="M10 7 L17 13 L10 19" fill="none" stroke="#f0f0f0" stroke-width="3" stroke-linecap="round" stroke-linejoin="round"/></svg>
          Waffle with toppings and yogurt: $6.26
        </li>
      </ul>
    </div>
  </div>
</body>
</html>
```